Social Business Consultancy

Kavora Ventures is a start up consultancy but with a difference: were non-corporate. We work in the field of economic development in low income countries and we focus on entrepreneurship but with a social and or environmental mission.

The type of projects we work on are innovative, ground breaking, different, edgy and bold. We are young, determined, , unreasonnable and undeterred by challenges.
We want our website to convey these ideas.
Updates

Hello,

Could you please include the option of having the website in two languages. Thank you.

Please note that new files have been added to the project brief.

- FrontPage  Main Photo (Grey dirt Road)
- WordCloud Photo to be used on the home page (as a small image )

The website should keep these colour tones.

Thank you !

Hello,

Wireframes have been uploaded. Please use as an indication.

Thanks,
n.

Target Market(s)

Governments, development agencies, social investors, NGOs, banks and social entrepreneurs.

Industry/Entity Type

Consulting

Requirements
Must have
• We already have a logo and business cards (provided). We want the website to look professional, yet simple with a maximum of two or three colours. We want the look to be seamless. There is no need for too many boxes or categories.
Nice to have
• We want bold, edgy, modern  and professional look .
• Examples:
• http://www.brightmarrowlab.org/
• http://www.pavelstone.com/
• http://www.tarnhiring.co.nz/
Should not have
• The design should not use old style fonts.

```html
<!DOCTYPE html>
<html lang="en">
<head>
<meta charset="utf-8">
<title>Kavora Ventures – Our Services</title>
<link rel="stylesheet" href="https://fonts.googleapis.com/css2?family=Arimo:wght@400;700&family=Roboto:wght@300;400&family=Cormorant+Garamond:wght@500&display=swap">
<style>
  :root {
    --lime: #c4d52a;
    --lime-dark: #8aa51f;
    --ink: #333333;
    --body-text: #4a4a4a;
    --nav-bg: #5f6063;
    --footer-bg: #626366;
    --rule: #dddddd;
    --navy: #1f2a44;
    --navy-light: #34405a;
    --white: #ffffff;
  }
  * { box-sizing: border-box; margin: 0; padding: 0; }
  html, body { width: 1200px; height: 921px; overflow: hidden; }
  body {
    position: relative;
    background: linear-gradient(#f1f1f1 0, #ffffff 116px, #eeeeee 117px, #ffffff 160px);
    font-family: "Roboto", Arial, sans-serif;
    color: var(--ink);
  }
  .brand {
    position: absolute; left: 185px; top: 30px;
    display: flex; align-items: center; gap: 10px;
    font-family: "Arimo", Arial, sans-serif; font-size: 30px; color: #6b6b6b;
  }
  .brand-mark { width: 40px; height: 40px; background: var(--lime); }
  .language {
    position: absolute; left: 847px; top: 25px;
    font-family: "Arimo", Arial, sans-serif; font-size: 12px; color: #111;
  }
  .language .active { color: #1a8fd6; font-weight: 700; }
  .language .option { font-weight: 700; }
  .main-nav {
    position: absolute; left: 620px; top: 66px; width: 404px; height: 35px;
    background: var(--nav-bg); border-radius: 6px;
    display: flex; align-items: center; padding-left: 20px;
    font-family: "Arimo", Arial, sans-serif; font-size: 14px;
  }
  .main-nav a { color: var(--white); text-decoration: none; padding: 0 10px; line-height: 35px; }
  .main-nav a.current { background: var(--lime); color: #111; padding: 0 6px; margin-right: 4px; }
  .page-title {
    position: absolute; left: 178px; top: 130px;
    font-family: "Arimo", Arial, sans-serif; font-size: 27px; font-weight: 400; color: #666;
  }
  .page-title span { color: var(--lime); }
  .title-rule { position: absolute; left: 176px; top: 164px; width: 848px; height: 1px; background: var(--rule); }
  .band { position: absolute; left: 0; top: 191px; width: 1200px; height: 163px; background: var(--lime); }
  .banner {
    position: absolute; left: 177px; top: 191px; width: 847px; height: 163px;
    background: linear-gradient(180deg, var(--navy-light) 0%, var(--navy) 100%);
  }
  .banner-headline {
    position: absolute; left: 24px; top: 24px;
    font-family: "Cormorant Garamond", Georgia, serif; font-weight: 500; font-size: 44px; color: var(--white);
  }
  .side-menu { position: absolute; left: 176px; top: 381px; width: 185px; }
  .box-heading {
    height: 27px; line-height: 28px; padding-left: 8px;
    background: linear-gradient(var(--lime), var(--lime-dark));
    color: var(--white); font-family: "Arimo", Arial, sans-serif; font-size: 21px; font-weight: 400;
  }
  .side-menu ul { list-style: none; }
  .side-menu li {
    height: 44px; padding: 16px 0 0 8px;
    font-family: "Arimo", Arial, sans-serif; font-size: 14px; color: #222;
    border-bottom: 1px dotted #888;
    background: linear-gradient(90deg, #fff 60%, #f2f2f2);
  }
  .content { position: absolute; left: 379px; top: 381px; width: 442px; }
  .content p {
    margin-top: 14px; font-size: 11px; line-height: 21.2px; font-weight: 300;
    color: var(--body-text); text-align: justify;
  }
  .content p + p { margin-top: 21px; }
  .photo {
    position: absolute; left: 839px; width: 185px; height: 185px;
    border: 1px solid #aaa; padding: 3px; background: var(--white);
  }
  .photo-fill { width: 100%; height: 100%; }
  .photo.tree { top: 381px; }
  .photo.tree .photo-fill { background: linear-gradient(180deg, #6f8a4a 0%, #b7b29a 55%, #5d5a68 100%); }
  .photo.figure { top: 609px; }
  .photo.figure .photo-fill { background: linear-gradient(160deg, #c9ccd6 0%, #eef0f4 55%, #d8d4c6 100%); }
  .footer { position: absolute; left: 0; top: 849px; width: 1200px; height: 72px; background: var(--footer-bg); }
  .footer-rule { position: absolute; left: 176px; top: 22px; width: 848px; height: 1px; background: #808184; }
  .copyright {
    position: absolute; left: 0; top: 40px; width: 1200px; text-align: center;
    font-size: 12px; color: var(--white); font-weight: 300;
  }
  .footer::before {
    content: ""; position: absolute; left: 0; top: -20px; width: 1200px; height: 20px;
    background: linear-gradient(#ffffff, #ececec);
  }
</style>
</head>
<body>
  <header>
    <div class="brand"><span class="brand-mark"></span>Kavora Ventures</div>
    <div class="language">Select Language : <span class="active">ENG</span> &nbsp;/&nbsp; <span class="option">FR</span></div>
    <nav class="main-nav">
      <a class="current" href="#">Home</a>
      <a href="#">About Us</a>
      <a href="#">Our Services</a>
      <a href="#">Event</a>
      <a href="#">Contact Us</a>
    </nav>
  </header>

  <h1 class="page-title">Our <span>Services</span></h1>
  <div class="title-rule"></div>

  <div class="band"></div>
  <div class="banner" role="img" aria-label="Banner photo: a row of matches, the last ones catching fire, on a dark blue background">
    <div class="banner-headline">Igniting opportunity</div>
  </div>

  <aside class="side-menu">
    <h2 class="box-heading">Main Menu</h2>
    <ul>
      <li>» What is Social Business</li>
      <li>» Our Approach</li>
      <li>» Our Services</li>
      <li>» Our Partners</li>
      <li>» Contact Us</li>
    </ul>
  </aside>

  <main class="content">
    <h2 class="box-heading">Our Services</h2>
    <p>Lorem Ipsum is simply dummy text of the printing and typesetting industry. Lorem Ipsum has been the industry's standard dummy text ever since the 1500s, when an unknown printer took a galley of type and scrambled it to make a type specimen book.</p>
    <p>It has survived not only five centuries, but also the leap into electronic typesetting, remaining essentially unchanged. It was popularised in the 1960s with the release of Typeline sheets containing Lorem Ipsum passages, and more recently with desktop publishing software like Quillset Layout including versions of Lorem Ipsum.</p>
    <p>Contrary to popular belief, Lorem Ipsum is not simply random text. It has roots in a piece of classical Latin literature from 45 BC, making it over 2000 years old. Marcus Holloway, a Latin professor at Westbrook College in Virginia, looked up one of the more obscure Latin words, consectetur, from a Lorem Ipsum passage, and going through the cites of the word in classical literature, discovered the undoubtable source. Lorem Ipsum comes from sections 1.10.32 and 1.10.33 of "de Finibus Bonorum et Malorum" (The Extremes of Good and Evil) by Varenus, written in 45 BC. This book is a treatise on the theory of ethics, very popular during the Renaissance. The first line of Lorem Ipsum, "Lorem ipsum dolor sit amet..", comes from a line in section 1.10.32.</p>
  </main>

  <figure class="photo tree"><div class="photo-fill" role="img" aria-label="Large banyan tree with hanging aerial roots"></div></figure>
  <figure class="photo figure"><div class="photo-fill" role="img" aria-label="Silhouette of a standing person against a bright sky"></div></figure>

  <footer class="footer">
    <div class="footer-rule"></div>
    <div class="copyright">© 2010 Kavora Ventures. &nbsp;All Rights Reserved.</div>
  </footer>
</body>
</html>
```